R. T. HOLLOWAY, INC. is a US based Investment firm looking for a five-page website design.

Currently, their temporary site is located at: rtholloway.example and they would like to maintain the site design as much as possible.

R. T. HOLLOWAY, INC. sister companies are: Crestway Lodge Investments (c-lodge.example) Benwick Petroleum (benwick-petroleum.example) and RTHF (rth-foundation.example/en)

Attached is a .ZIP file with designs and assets we think will be useful for your proposal… Content for the site is attached on: rtholloway website content.docx Current temp website design is attached as: Coming Soon Website.zip .EPS Logo files attached as: rtholloway logos.zip Sample business card attached as: R T Holloway Business cards.eps Other assets, such as Fonts and background images attached as: Assets.zip

Target Market(s)

Investors

Industry/Entity Type

Investments

Number of Pages Required

5+ page

Requirements
Must have
• Contact Page with a form.

```html
<!DOCTYPE html>
<html lang="en">
<head>
<meta charset="utf-8">
<title>R. T. Holloway, Inc. — Investments</title>
<link rel="stylesheet" href="https://fonts.googleapis.com/css2?family=Cinzel:wght@400;600;700&family=Montserrat:wght@400;600;700;800&family=Open+Sans:ital,wght@0,400;0,600;0,700;1,600;1,700&display=swap">
<style>
:root{
  --gold:#b79a5b;
  --gold-dark:#9d8248;
  --ink:#2b2f36;
  --text:#6b6f76;
  --navy:#1c2634;
  --navy-2:#2c3a4d;
  --line:#e3e0d8;
  --soft:#f4f2ee;
  --white:#ffffff;
}
*{box-sizing:border-box;margin:0;padding:0}
html,body{width:1200px;height:4320px;overflow:hidden}
body{position:relative;font-family:"Open Sans",Arial,sans-serif;color:var(--text);background:var(--white)}
.abs{position:absolute}
.btn{position:absolute;display:inline-flex;align-items:center;justify-content:center;background:var(--gold);color:var(--white);font-family:"Montserrat",Arial,sans-serif;font-size:13px;font-weight:700;letter-spacing:1px;text-transform:uppercase;border-radius:22px;white-space:nowrap}
.eyebrow{position:absolute;font-size:15px;color:var(--gold);font-weight:600}
.section-title{position:absolute;font-family:"Cinzel",Georgia,serif;color:var(--ink);font-weight:400;white-space:nowrap}
.para{position:absolute;font-size:14px;line-height:24px;color:var(--text)}
.photo{position:absolute;overflow:hidden}

/* hero */
.hero{position:absolute;left:0;top:0;width:1200px;height:800px;overflow:hidden;background:linear-gradient(180deg,#1f2b3b 0%,#34465c 45%,#8a7358 78%,#c49a62 100%)}
.hero-glow{position:absolute;left:0;top:0;width:1200px;height:800px;background:radial-gradient(ellipse at 60% 75%,rgba(236,170,90,.55),rgba(0,0,0,0) 60%)}
.hero-shade{position:absolute;left:0;top:0;width:700px;height:800px;background:linear-gradient(90deg,rgba(20,28,40,.75),rgba(20,28,40,0))}
.brand{position:absolute;left:48px;top:14px;display:flex;align-items:center;gap:10px}
.brand-dot{width:40px;height:40px;border-radius:50%;border:2px solid var(--gold)}
.brand-name{font-family:"Open Sans",Arial,sans-serif;font-weight:700;font-size:14px;color:var(--white);letter-spacing:1px;white-space:nowrap}
.nav{position:absolute;left:396px;top:0;width:804px;height:44px;background:rgba(18,24,33,.85);display:flex;align-items:center;font-family:"Montserrat",Arial,sans-serif;font-size:11px;font-weight:600;color:var(--white);letter-spacing:.5px;white-space:nowrap}
.nav a{height:44px;display:flex;align-items:center;padding:0 14px;color:var(--white);text-decoration:none}
.nav a.active{background:var(--gold)}
.nav .nav-phone{margin-left:auto;background:var(--gold);padding:0 22px;font-size:13px;font-weight:700;gap:8px}
.hero h1{position:absolute;left:64px;top:222px;font-family:"Montserrat",Arial,sans-serif;font-weight:800;color:var(--white);font-size:46px;line-height:54px;letter-spacing:1px;white-space:nowrap}
.hero-sub{position:absolute;left:64px;top:344px;width:460px;font-size:15px;line-height:24px;color:#e9e6df}
.hero-caption{position:absolute;left:792px;top:290px;font-family:"Cinzel",Georgia,serif;font-size:46px;color:var(--white)}
.hero-arrow{position:absolute;left:1090px;width:28px;height:28px;border-radius:4px;background:rgba(255,255,255,.2);display:flex;align-items:center;justify-content:center}

/* cards */
.card{position:absolute;top:1412px;width:248px;height:290px;border:1px solid var(--line);border-radius:6px;background:var(--white);box-shadow:0 4px 14px rgba(0,0,0,.05);text-align:center}
.card svg.icon{margin-top:18px}
.card h3{font-family:"Cinzel",Georgia,serif;font-weight:400;font-size:20px;line-height:26px;color:var(--ink);margin-top:8px;letter-spacing:1px}
.card p{font-size:12px;line-height:18px;color:var(--text);padding:8px 18px 0}
.card .go{position:absolute;left:104px;bottom:16px;width:40px;height:40px;border-radius:50%;background:var(--gold);display:flex;align-items:center;justify-content:center}

/* form */
.field{position:absolute;left:88px;width:480px;height:44px;border:1px solid var(--line);border-radius:4px;font-size:13px;color:#9a9ca1;padding:12px 16px;background:var(--white)}
.field .caret{position:absolute;right:16px;top:18px}

/* footer */
.footer h4{position:absolute;font-family:"Cinzel",Georgia,serif;font-weight:700;font-size:18px;color:var(--ink);white-space:nowrap}
.footer ul{position:absolute;list-style:none;font-size:13px;line-height:28px;color:var(--text)}
.footer li::before{content:"›";color:var(--gold);margin-right:8px;font-weight:700}
.social{position:absolute;width:34px;height:34px;border-radius:50%;border:2px solid var(--gold)}
.contact-line{position:absolute;display:flex;gap:12px;font-size:13px;line-height:20px;color:var(--text);white-space:nowrap}
.bottom-bar{position:absolute;left:0;top:4280px;width:1200px;height:40px;background:var(--gold);color:var(--white);font-size:12px;display:flex;align-items:center;justify-content:center;letter-spacing:.5px}
</style>
</head>
<body>

<!-- HERO -->
<section class="hero">
  <div class="hero-glow" role="img" aria-label="Industrial plant with smokestacks at dusk"></div>
  <div class="hero-shade"></div>
  <svg class="abs" style="left:0;top:0" width="1200" height="800" viewBox="0 0 1200 800">
    <circle cx="930" cy="340" r="290" fill="none" stroke="var(--gold)" stroke-width="6" stroke-dasharray="1300 520" transform="rotate(-60 930 340)"/>
  </svg>
  <div class="brand"><div class="brand-dot"></div><div class="brand-name">R. T. HOLLOWAY, INC.</div></div>
  <nav class="nav">
    <a class="active">HOME</a><a>ABOUT US</a><a>INVESTMENT AREAS</a><a>SOCIAL RESPONSIBILITY</a><a>CONTACT US</a>
    <a class="nav-phone"><svg width="14" height="14" viewBox="0 0 24 24"><path d="M6.6 10.8a15 15 0 0 0 6.6 6.6l2.2-2.2c.3-.3.7-.4 1-.2 1.1.4 2.3.6 3.6.6.6 0 1 .4 1 1V20c0 .6-.4 1-1 1A17 17 0 0 1 3 4c0-.6.4-1 1-1h3.5c.6 0 1 .4 1 1 0 1.3.2 2.5.6 3.6.1.3 0 .7-.2 1z" fill="#fff"/></svg>+1 (000) 000 0000</a>
  </nav>
  <h1>WELCOME TO<br>R. T. HOLLOWAY, INC.</h1>
  <p class="hero-sub">R. T. Holloway, Inc. helps grow ideas into a great market with new investments, raising its footprint worldwide.</p>
  <div class="btn" style="left:64px;top:410px;width:150px;height:40px">Contact Us</div>
  <div class="hero-caption">Industry</div>
  <div class="hero-arrow" style="top:282px"><svg width="10" height="14" viewBox="0 0 10 14"><path d="M2 1l6 6-6 6" stroke="#fff" stroke-width="2" fill="none"/></svg></div>
  <div class="hero-arrow" style="top:320px"><svg width="10" height="14" viewBox="0 0 10 14"><path d="M8 1L2 7l6 6" stroke="#fff" stroke-width="2" fill="none"/></svg></div>
  <svg class="abs" style="left:0;top:640px" width="1200" height="160" viewBox="0 0 1200 160">
    <path d="M0 110 C 300 40 900 40 1200 110 L1200 160 L0 160 Z" fill="#fff"/>
    <path d="M0 110 C 300 40 900 40 1200 110" fill="none" stroke="var(--gold)" stroke-width="4"/>
    <circle cx="600" cy="66" r="20" fill="#fff" stroke="var(--gold)" stroke-width="2"/>
    <path d="M592 62l8 8 8-8" stroke="var(--gold)" stroke-width="2" fill="none"/>
  </svg>
</section>

<!-- ABOUT -->
<section>
  <div class="eyebrow" style="left:128px;top:826px">About Us</div>
  <h2 class="section-title" style="left:128px;top:846px;font-size:42px">R T Holloway</h2>
  <p class="para" style="left:128px;top:918px;width:560px">Based in Houston, Texas, R. T. Holloway, Inc. is an investment company, founded in 2010, with the purpose of clear fundamentals for sustained development and steady guidance for increasing the potential of world resources, designed to meet the demands of the emerging markets. R. T. Holloway, Inc. functions as a robust and versatile investment, with the goal of achieving the multiple opportunities available.</p>
  <p class="para" style="left:128px;top:1054px;width:560px">R. T. Holloway, Inc. holds interests in areas of investment that are vital to the international economy: <b style="color:var(--ink)">Sectors of Energy, Mining, Industry, Finance and Real Estate.</b></p>
  <div class="btn" style="left:128px;top:1134px;width:140px;height:38px">Learn More</div>
  <svg class="abs" style="left:730px;top:800px" width="460" height="440" viewBox="0 0 460 440">
    <circle cx="230" cy="220" r="206" fill="none" stroke="var(--gold)" stroke-width="7" stroke-dasharray="900 400" transform="rotate(150 230 220)"/>
  </svg>
  <div class="photo" style="left:772px;top:832px;width:376px;height:376px;border-radius:50%;background:linear-gradient(135deg,#e9edf0,#c9d2d9 55%,#9aa6b0)" role="img" aria-label="Team working at computers in a bright office"></div>
</section>

<!-- INVESTMENT AREAS -->
<section>
  <svg class="abs" style="left:-60px;top:1330px" width="200" height="200" viewBox="0 0 200 200"><circle cx="100" cy="100" r="80" fill="none" stroke="#ececec" stroke-width="22"/></svg>
  <div class="eyebrow" style="left:88px;top:1290px">What We Do</div>
  <h2 class="section-title" style="left:88px;top:1310px;font-size:44px;letter-spacing:1px">INVESTMENT AREAS</h2>
  <div class="abs" style="left:88px;top:1372px;width:1024px;height:1px;background:var(--line)"></div>
  <div class="btn" style="left:916px;top:1326px;width:196px;height:36px">View All Services &nbsp;›</div>

  <div class="card" style="left:88px">
    <svg class="icon" width="56" height="48" viewBox="0 0 64 56" fill="none" stroke="var(--gold)" stroke-width="2"><path d="M36 4L18 32h14l-4 20 18-28H32z"/></svg>
    <h3>ENERGY</h3>
    <p>R. T. Holloway, Inc. holds investments in projects of oil and gas exploration, production and supply while focusing on clean power generation.</p>
    <div class="go"><svg width="14" height="12" viewBox="0 0 14 12"><path d="M1 6h11M7 1l5 5-5 5" stroke="#fff" stroke-width="2" fill="none"/></svg></div>
  </div>
  <div class="card" style="left:360px">
    <svg class="icon" width="56" height="48" viewBox="0 0 64 56" fill="none" stroke="var(--gold)" stroke-width="2"><path d="M8 20h48l-6 20H14z"/><circle cx="20" cy="46" r="5"/><circle cx="44" cy="46" r="5"/><path d="M18 20l8-12 10 6 8-8"/></svg>
    <h3>MINING</h3>
    <p>R. T. Holloway, Inc. holds interest in the management of operations of minerals mines, with current production of steel and gold ore.</p>
    <div class="go"><svg width="14" height="12" viewBox="0 0 14 12"><path d="M1 6h11M7 1l5 5-5 5" stroke="#fff" stroke-width="2" fill="none"/></svg></div>
  </div>
  <div class="card" style="left:632px">
    <svg class="icon" width="56" height="48" viewBox="0 0 64 56" fill="none" stroke="var(--gold)" stroke-width="2"><path d="M6 52V28l14 8v-8l14 8v-8l14 8V8h8v44z"/><path d="M14 44h6M28 44h6M42 44h6"/></svg>
    <h3>INDUSTRY</h3>
    <p>R. T. Holloway, Inc. holds investments in cement manufacturing plants with new distribution in Texas, Louisiana and Colorado.</p>
    <div class="go"><svg width="14" height="12" viewBox="0 0 14 12"><path d="M1 6h11M7 1l5 5-5 5" stroke="#fff" stroke-width="2" fill="none"/></svg></div>
  </div>
  <div class="card" style="left:904px">
    <svg class="icon" width="56" height="48" viewBox="0 0 64 56" fill="none" stroke="var(--gold)" stroke-width="2"><path d="M4 26l12-10 10 4 10-4 6 2"/><path d="M60 26L48 16l-10 2-10 10c-2 2 0 5 3 4l8-5 12 10"/><path d="M16 30l14 14c2 2 5 0 4-2M22 36l10 10"/></svg>
    <h3>FINANCE</h3>
    <p>R. T. Holloway, Inc. serves as a platform for ventures through commodity exchange. Main partners include trusted funding banks.</p>
    <div class="go"><svg width="14" height="12" viewBox="0 0 14 12"><path d="M1 6h11M7 1l5 5-5 5" stroke="#fff" stroke-width="2" fill="none"/></svg></div>
  </div>
</section>

<!-- WORK TOGETHER -->
<section>
  <div class="photo" style="left:0;top:1740px;width:1200px;height:510px;background:linear-gradient(180deg,#3b4d63 0%,#2a3a4f 45%,#1c2634 100%)" role="img" aria-label="Solar panel field under an evening sky"></div>
  <div class="abs" style="left:0;top:1740px;width:1200px;height:510px;background:radial-gradient(ellipse at 50% 20%,rgba(214,168,110,.35),rgba(0,0,0,0) 55%)"></div>
  <svg class="abs" style="left:0;top:1730px" width="1200" height="530" viewBox="0 0 1200 530">
    <path d="M0 0 H1200 V40 C 900 110 300 110 0 40 Z" fill="#fff"/>
    <path d="M0 40 C 300 110 900 110 1200 40" fill="none" stroke="var(--gold)" stroke-width="4"/>
    <path d="M0 530 H1200 V460 C 900 390 300 390 0 460 Z" fill="#fff"/>
    <path d="M0 460 C 300 390 900 390 1200 460" fill="none" stroke="var(--gold)" stroke-width="4"/>
  </svg>
  <h2 class="abs" style="left:0;top:1956px;width:1200px;text-align:center;font-family:'Montserrat',Arial,sans-serif;font-weight:700;font-size:44px;color:var(--white)">Let's Work Together</h2>
  <p class="abs" style="left:360px;top:2024px;width:480px;text-align:center;font-size:13px;line-height:21px;color:#d9dde3">Lorem ipsum has been the industry's standard dummy text ever since the 1500s, when an unknown printer took a galley of type and scrambled it.</p>
  <div class="abs" style="left:0;top:2080px;width:1200px;text-align:center;font-family:'Montserrat',Arial,sans-serif;font-weight:700;font-size:40px;color:var(--gold)">+1 (000) 000 0000</div>
</section>

<!-- SOCIAL RESPONSIBILITY -->
<section>
  <svg class="abs" style="left:1060px;top:2190px" width="180" height="180" viewBox="0 0 180 180"><circle cx="90" cy="90" r="70" fill="none" stroke="#ececec" stroke-width="20"/></svg>
  <svg class="abs" style="left:110px;top:2326px" width="460" height="460" viewBox="0 0 460 460">
    <circle cx="230" cy="230" r="214" fill="none" stroke="var(--gold)" stroke-width="7" stroke-dasharray="860 500" transform="rotate(-30 230 230)"/>
  </svg>
  <div class="photo" style="left:150px;top:2366px;width:380px;height:380px;border-radius:50%;background:radial-gradient(circle at 50% 50%,#7a5a3c,#b58a66 45%,#d7c2ad 75%,#eadfd2)" role="img" aria-label="Many hands holding soil with a young plant"></div>
  <div class="eyebrow" style="left:640px;top:2410px">Who Us</div>
  <h2 class="section-title" style="left:640px;top:2430px;font-size:42px;line-height:50px">Social<br>Responsibility</h2>
  <p class="para" style="left:640px;top:2550px;width:470px">Since the commencement of R. T. Holloway, Inc., we contribute to change the quality of life of children and seniors across the world, providing them with support for primary education and basic medical aid, which we believe to be the right of every human being.</p>
  <p class="para" style="left:640px;top:2670px;width:470px">Proportionally to our growth, R. T. Holloway, Inc. aims to extend our contributions to other communities in Africa and the rest of the World, with new initiatives as charities and other non-profit organizations via the RTHF Foundation.</p>
  <div class="abs" style="left:640px;top:2768px;font-size:14px;color:#2f6bd0;text-decoration:underline">https://rth-foundation.example/en</div>
</section>

<!-- CONTACT -->
<section>
  <div class="eyebrow" style="left:88px;top:2876px">Get in Touch?</div>
  <h2 class="section-title" style="left:88px;top:2896px;font-size:48px">CONTACT US</h2>
  <p class="para" style="left:88px;top:2966px;width:480px">Get in touch with our representatives and start your journey on expanding your company and making your business dream come agile and profitable.</p>
  <div class="field" style="top:3040px">Name *</div>
  <div class="field" style="top:3096px">Phone *</div>
  <div class="field" style="top:3152px">Email *<svg class="caret" width="10" height="6" viewBox="0 0 10 6"><path d="M0 0l5 6 5-6z" fill="#9a9ca1"/></svg></div>
  <div class="field" style="top:3208px">Services *<svg class="caret" width="10" height="6" viewBox="0 0 10 6"><path d="M0 0l5 6 5-6z" fill="#9a9ca1"/></svg></div>
  <div class="field" style="top:3264px;height:90px">Message *</div>
  <div class="btn" style="left:88px;top:3370px;width:110px;height:38px">Submit</div>
  <div class="photo" style="left:744px;top:2872px;width:456px;height:470px;background:linear-gradient(135deg,#d9d2c6,#b9a98f 50%,#7d6c58)" role="img" aria-label="Smiling man with glasses working on a laptop in an office"></div>
  <svg class="abs" style="left:744px;top:2872px" width="456" height="470" viewBox="0 0 456 470">
    <circle cx="240" cy="250" r="190" fill="none" stroke="var(--gold)" stroke-width="7" stroke-dasharray="820 380" transform="rotate(170 240 250)"/>
  </svg>
</section>

<!-- MISSION BAND -->
<section>
  <div class="photo" style="left:0;top:3460px;width:1200px;height:570px;background:linear-gradient(180deg,#c4c8cc 0%,#8f8a84 50%,#4a4744 100%)" role="img" aria-label="Business team meeting around a conference table"></div>
  <svg class="abs" style="left:0;top:3450px" width="1200" height="120" viewBox="0 0 1200 120">
    <path d="M0 0 H1200 V50 C 900 120 300 120 0 50 Z" fill="#fff"/>
  </svg>
  <div class="abs" style="left:424px;top:3536px;width:360px;height:360px;border-radius:50%;background:rgba(183,154,91,.85)"></div>
  <p class="abs" style="left:454px;top:3606px;width:300px;text-align:center;font-style:italic;font-weight:700;font-size:19px;line-height:29px;color:var(--white)">R. T. Holloway, Inc. is the Main Private investment company Working Towards the Diversification and Consolidation of National and Regional Economy</p>
</section>

<!-- FOOTER -->
<footer class="footer">
  <div class="abs" style="left:0;top:4030px;width:1200px;height:250px;background:var(--white)"></div>
  <div class="abs" style="left:118px;top:4052px;width:56px;height:56px;border-radius:50%;border:2px solid var(--gold)"></div>
  <div class="abs" style="left:36px;top:4118px;width:220px;text-align:center;font-weight:700;font-size:14px;color:var(--ink);letter-spacing:1px;white-space:nowrap">R. T. HOLLOWAY, INC.</div>
  <div class="social" style="left:86px;top:4152px"></div>
  <div class="social" style="left:129px;top:4152px"></div>
  <div class="social" style="left:172px;top:4152px"></div>

  <h4 style="left:380px;top:4050px">Sitemap</h4>
  <ul style="left:380px;top:4086px"><li>Home</li><li>About Us</li><li>Investment Areas</li><li>Social Responsibility</li><li>Contact Us</li></ul>

  <h4 style="left:620px;top:4050px">Contact Us</h4>
  <div class="contact-line" style="left:620px;top:4090px"><svg width="14" height="18" viewBox="0 0 14 18"><path d="M7 0a7 7 0 0 0-7 7c0 5 7 11 7 11s7-6 7-11a7 7 0 0 0-7-7zm0 9.5A2.5 2.5 0 1 1 7 4.5a2.5 2.5 0 0 1 0 5z" fill="var(--gold)"/></svg><span>R. T. HOLLOWAY, INC.<br>2150 Harbor Point Dr, Suite 400<br>Houston, TX 77002</span></div>
  <div class="contact-line" style="left:620px;top:4170px"><svg width="14" height="14" viewBox="0 0 24 24"><path d="M6.6 10.8a15 15 0 0 0 6.6 6.6l2.2-2.2c.3-.3.7-.4 1-.2 1.1.4 2.3.6 3.6.6.6 0 1 .4 1 1V20c0 .6-.4 1-1 1A17 17 0 0 1 3 4c0-.6.4-1 1-1h3.5c.6 0 1 .4 1 1 0 1.3.2 2.5.6 3.6.1.3 0 .7-.2 1z" fill="var(--gold)"/></svg><span>+1 (000) 000 0000</span></div>
  <div class="contact-line" style="left:620px;top:4200px"><svg width="16" height="12" viewBox="0 0 16 12"><rect x="1" y="1" width="14" height="10" fill="none" stroke="var(--gold)" stroke-width="2"/><path d="M1 1l7 6 7-6" stroke="var(--gold)" stroke-width="2" fill="none"/></svg><span>contact@rtholloway.example</span></div>

  <h4 style="left:890px;top:4050px">Newsletter Sign up ?</h4>
  <p class="para" style="left:890px;top:4086px;width:260px;font-size:12px;line-height:19px">Sign up to stay updated with R. T. Holloway news.</p>
  <div class="abs" style="left:890px;top:4132px;width:240px;height:38px;border:1px solid var(--line);border-radius:20px;font-size:12px;color:#9a9ca1;padding:10px 16px">Enter Email *</div>
  <div class="btn" style="left:890px;top:4184px;width:120px;height:36px">Subscribe</div>

  <div class="bottom-bar">R. T. HOLLOWAY, INC. · 2024 All rights reserved</div>
</footer>

</body>
</html>
```